Economics of an Assumption vs Obtaining a New Loan at Current Market Rate

I need to marketing flyer that has fields that calculate mortgage payments amongst other calculations. I have a rough draft that I will attach.

The idea is to provide a tool for a real estate agent to use to illustrate to a potential buyer what a payment would be if they assumed the existing loan on the house or took out a new loan at current market.

The flyer needs to be able to allow an agent to drop in their logo, photo, and contact along with the loan officers photo and contact info.

You can google open house flyer to see examples of what the overall artwork and presentation can look like.

Target Market(s)

Home Buyers

Industry/Entity Type

Real Estate

Colors
F0912C
F2A743
F7CA91
FBE8D2
FDF5EE
EE7325
F08F49
F5BC92
FAE3D3
FDF4ED

Requirements
Must have
• A way to calculate mortgage payment
Nice to have
• Photo and logo drop ins

```html
<!DOCTYPE html>
<html lang="en">
<head>
<meta charset="UTF-8">
<title>Assumption vs New Loan – Payment Flyer</title>
<link href="https://fonts.googleapis.com/css2?family=Poppins:wght@400;500;600;700;800&display=swap" rel="stylesheet">
<style>
  :root{
    --stage:#5c5c5c;
    --paper:#ffffff;
    --orange:#e99b16;
    --orange-deep:#c4601e;
    --orange-bright:#f2a743;
    --brand:#ee7325;
    --peach:#f7cf9c;
    --ink:#1f1f1f;
    --label:#5a2c0c;
    --field-border:#d9d9d9;
    --logo-slot:#dcdedd;
    --brush:#2b2b2b;
  }
  *{box-sizing:border-box;margin:0;padding:0}
  html,body{width:973px;height:1200px;overflow:hidden;background:var(--stage)}
  body{font-family:'Poppins',sans-serif;position:relative}
  .flyer{position:absolute;left:23px;top:0;width:927px;height:1200px;background:var(--paper);overflow:hidden}
  .flyer-art{position:absolute;inset:0}
  .abs{position:absolute}
  .logo-slot{left:160px;top:37px;width:299px;height:81px;background:var(--logo-slot)}
  .logo-caption{left:160px;top:131px;width:299px;text-align:center;font-weight:700;font-size:22px;color:var(--ink)}
  .brand-name{left:662px;top:62px;width:220px;text-align:center;font-weight:500;font-size:46px;line-height:1.2;color:var(--brand);letter-spacing:.5px;white-space:nowrap}
  .price-label{left:333px;top:258px;font-weight:800;font-size:31px;color:#fff;letter-spacing:.3px}
  .price-field{left:656px;top:253px;width:226px;height:52px;background:#fff;border:3px solid var(--orange-bright);border-radius:9px}
  .section-bar{height:42px;background:var(--brush);clip-path:polygon(2% 8%,97% 0,100% 45%,96% 100%,4% 94%,0 55%)}
  .section-title{color:#fff;font-weight:800;font-size:18px;line-height:1}
  .section-sub{color:#fff;font-weight:400;font-size:13px;line-height:1}
  .row-label{font-weight:800;font-size:16.5px;color:var(--label);line-height:1;white-space:nowrap}
  .row-label.total{color:var(--ink);font-size:18px}
  .field{height:21px;background:#fff;border:1.5px solid var(--field-border);border-radius:3px;font-size:12.5px;color:var(--ink);padding-left:10px;line-height:18px;white-space:nowrap}
  .field.strong{font-weight:700}
  .note{font-size:14px;color:var(--ink)}
  .difference-band{left:90px;top:954px;width:785px;height:39px;background:var(--peach)}
  .difference-label{left:184px;top:959px;font-weight:800;font-size:22px;color:var(--ink)}
  .contact-head{font-weight:700;font-size:13px;color:var(--orange-deep);border-bottom:1.5px solid var(--orange-deep);width:141px;padding-bottom:1px}
  .contact-line{font-size:11px;color:#fff;line-height:17.5px;white-space:nowrap}
  .badge-text{left:740px;top:1062px;width:190px;text-align:center;color:#fff;font-size:19px;line-height:26px;white-space:nowrap}
  .badge-text b{font-weight:700}
</style>
</head>
<body>
<div class="flyer">
  <svg class="flyer-art" viewBox="0 0 927 1200" width="927" height="1200">
    <defs>
      <linearGradient id="photoTone" x1="0" y1="0" x2="0" y2="1">
        <stop offset="0" stop-color="#8d9fd0"/>
        <stop offset=".32" stop-color="#b9b0c4"/>
        <stop offset=".45" stop-color="#b48a60"/>
        <stop offset=".8" stop-color="#a07a58"/>
        <stop offset="1" stop-color="#9a9590"/>
      </linearGradient>
      <linearGradient id="ribbonTone" x1="0" y1="0" x2="1" y2="0">
        <stop offset="0" stop-color="#3c3c3c"/>
        <stop offset=".45" stop-color="#e6e6e6"/>
        <stop offset=".75" stop-color="#9a9a9a"/>
        <stop offset="1" stop-color="#3a3a3a"/>
      </linearGradient>
    </defs>
    <rect x="0" y="150" width="927" height="610" fill="url(#photoTone)" role="img" aria-label="Photo of the listed property: a stucco house with tiled roof under a cloudy sky"/>
    <path d="M0,0 H927 V253 C750,210 500,198 300,208 C200,214 100,250 0,279 Z" fill="url(#ribbonTone)"/>
    <path d="M0,0 H927 V160 C720,172 520,232 300,224 C180,218 80,192 0,178 Z" fill="#fff"/>
    <path d="M0,41 C120,120 220,212 315,212 C420,212 560,80 664,0" fill="none" stroke="var(--orange-deep)" stroke-width="7"/>
    <path d="M0,600 C150,575 300,560 450,575 C650,595 800,612 927,606 V700 H0 Z" fill="url(#ribbonTone)"/>
    <path d="M0,665 C200,618 400,602 500,622 C700,660 850,690 927,685 V1200 H0 Z" fill="var(--orange)"/>
    <path d="M0,665 C200,618 400,602 500,622 C700,660 850,690 927,685" fill="none" stroke="var(--orange-deep)" stroke-width="7"/>
    <circle cx="141" cy="1080" r="72" fill="var(--orange-deep)"/>
    <circle cx="141" cy="1078" r="70" fill="#fff"/>
    <circle cx="141" cy="1078" r="64" fill="#7a7a7a" role="img" aria-label="Agent photo placeholder"/>
    <circle cx="615" cy="1080" r="72" fill="var(--orange-deep)"/>
    <circle cx="615" cy="1078" r="70" fill="#fff"/>
    <circle cx="615" cy="1078" r="64" fill="#7a7a7a" role="img" aria-label="Loan officer photo placeholder"/>
    <circle cx="850" cy="1170" r="133" fill="#fff"/>
    <circle cx="853" cy="1170" r="131" fill="var(--orange-deep)"/>
  </svg>

  <div class="abs logo-slot"></div>
  <div class="abs logo-caption">Drop in Logo</div>
  <div class="abs brand-name">Orvenna</div>

  <div class="abs price-label">PURCHASE PRICE:</div>
  <div class="abs price-field"></div>

  <div class="abs section-bar" style="left:65px;top:698px;width:280px"></div>
  <div class="abs section-title" style="left:101px;top:710px">CURRENT MORTGAGE:</div>
  <div class="abs section-bar" style="left:470px;top:697px;width:273px"></div>
  <div class="abs section-title" style="left:509px;top:702px">NEW MORTGAGE</div>
  <div class="abs section-sub" style="left:511px;top:720px">10% Down Payment</div>

  <!-- current mortgage -->
  <div class="abs row-label" style="left:102px;top:746px">Loan Amount :</div>
  <div class="abs row-label" style="left:102px;top:771px">Interest Rate :</div>
  <div class="abs row-label" style="left:102px;top:796px">Principal Interest :</div>
  <div class="abs row-label" style="left:102px;top:821px">Mortgage Insurance :</div>
  <div class="abs row-label total" style="left:102px;top:853px">TOTAL</div>
  <div class="abs field" style="left:295px;top:745px;width:173px">Allow Input</div>
  <div class="abs field" style="left:295px;top:770px;width:173px">Allow Input</div>
  <div class="abs field" style="left:295px;top:795px;width:173px">Allow Input</div>
  <div class="abs field" style="left:295px;top:820px;width:173px">Allow Input</div>
  <div class="abs field strong" style="left:295px;top:852px;width:173px">Amount</div>
  <div class="abs row-label" style="left:102px;top:884px">Years</div>
  <div class="abs field" style="left:157px;top:882px;width:59px">Input</div>
  <div class="abs row-label" style="left:223px;top:884px">Months</div>
  <div class="abs field" style="left:296px;top:882px;width:60px">Input</div>
  <div class="abs note" style="left:367px;top:883px">Left on load</div>
  <div class="abs row-label" style="left:102px;top:919px">Delta</div>
  <div class="abs field" style="left:166px;top:917px;width:304px">Purchase price minus loan amount</div>

  <!-- new mortgage -->
  <div class="abs row-label" style="left:507px;top:746px">Loan Amount :</div>
  <div class="abs row-label" style="left:507px;top:771px">Market Rate :</div>
  <div class="abs row-label" style="left:507px;top:796px">Principal Interest :</div>
  <div class="abs row-label" style="left:507px;top:821px">Mortgage Insurance :</div>
  <div class="abs row-label total" style="left:507px;top:853px">TOTAL</div>
  <div class="abs field" style="left:702px;top:745px;width:173px">Allow Input</div>
  <div class="abs field" style="left:702px;top:770px;width:173px">Allow Input</div>
  <div class="abs field" style="left:702px;top:795px;width:173px">Allow Input</div>
  <div class="abs field" style="left:702px;top:820px;width:173px">Allow Input</div>
  <div class="abs field strong" style="left:702px;top:852px;width:173px">Amount</div>
  <div class="abs row-label" style="left:507px;top:884px">Term</div>
  <div class="abs field" style="left:555px;top:882px;width:60px">Input</div>
  <div class="abs row-label" style="left:629px;top:884px">Years</div>
  <div class="abs field" style="left:687px;top:882px;width:60px">Input</div>
  <div class="abs row-label" style="left:507px;top:919px">Down Payment Amount</div>
  <div class="abs field" style="left:773px;top:917px;width:102px">Input</div>

  <div class="abs difference-band"></div>
  <div class="abs difference-label">Payment Difference</div>
  <div class="abs field" style="left:445px;top:961px;width:332px;height:23px;line-height:20px">Difference between totals</div>

  <div class="abs" style="left:223px;top:1043px">
    <div class="contact-head">PROPRIETOR</div>
    <div class="contact-line" style="margin-top:3px">Name:..............................</div>
    <div class="contact-line">Phone:..............................</div>
    <div class="contact-line">Email ID:...........................</div>
    <div class="contact-line">Web:...............................</div>
  </div>
  <div class="abs" style="left:393px;top:1043px">
    <div class="contact-head">PROPRIETOR</div>
    <div class="contact-line" style="margin-top:3px">Name:..............................</div>
    <div class="contact-line">Phone:..............................</div>
    <div class="contact-line">Email ID:...........................</div>
    <div class="contact-line">Web:...............................</div>
  </div>

  <div class="abs badge-text">This Property<br>is <b>“Keep the<br>low rate<br>approved”</b></div>
</div>
</body>
</html>
```